Book Cover Design for The Banker's Riddle

We need a bold, attention-getting design for a book on a revolutionary new way of funding government spending - not only could we eliminate income taxes and finally balance the budget, but we could afford to pay everyone a basic income, provide free healthcare, free college, and a guaranteed retirement. See www.TheBankersRiddle.net to understand the proposition.

The book title is: The Banker's Riddle

The subtitle is: If Our Country Were Managed Wisely, We Wouldn't Owe Taxes, We'd Collect Returns

The author's name is: Derek Hale

Target Market(s)

General population

Industry/Entity Type

Government

Font styles to use
Sans Serif

Requirements
Must have
• The blurb about the book, and about the author should be on the back cover, as should the author's photo.
• The book will be 5.5 x 8.5 inches and 165 pages long
Nice to have
• The subtitle should be prominent on the front cover, perhaps even above the title. The designer can use the sunrise photo as we do on the website to feature the subtitle, or not. We are open to all designs.

```html
<!DOCTYPE html>
<html lang="en">
<head>
<meta charset="utf-8">
<title>The Banker's Riddle — Cover Wrap</title>
<link rel="stylesheet" href="https://fonts.googleapis.com/css2?family=Fira+Sans+Extra+Condensed:wght@600;700;800&family=Source+Sans+3:wght@300;400;600;700&display=swap">
<style>
  :root {
    --ink: #111111;
    --paper: #ffffff;
    --back-top: #e6a53c;
    --back-mid: #dd8a2a;
    --back-low: #d0661c;
    --sun-core: #fffbe8;
    --sun-glow: #f7c54a;
    --front-mid: #e8902a;
    --front-deep: #b8420f;
    --front-shadow: #7a2408;
    --spine-tint: rgba(150, 90, 30, 0.35);
    --photo-frame: #e0891e;
    --photo-fill: #6b6a4a;
  }
  * { box-sizing: border-box; margin: 0; padding: 0; }
  html, body { width: 1200px; height: 887px; overflow: hidden; background: #ffffff; }
  .cover-wrap { position: relative; width: 1200px; height: 887px; overflow: hidden; font-family: "Source Sans 3", sans-serif; }

  .back-scene, .front-scene { position: absolute; top: 0; height: 887px; }
  .back-scene {
    left: 0; width: 626px;
    background:
      radial-gradient(ellipse 420px 260px at 300px 260px, rgba(246, 200, 90, 0.45), transparent 70%),
      linear-gradient(180deg, var(--back-top) 0%, var(--back-mid) 40%, var(--back-low) 100%);
  }
  .front-scene {
    left: 626px; width: 574px;
    background:
      radial-gradient(circle 75px at 175px 214px, var(--sun-core) 0%, rgba(255, 248, 220, 0.9) 40%, transparent 100%),
      radial-gradient(circle 340px at 175px 214px, rgba(250, 215, 110, 0.9) 0%, rgba(240, 170, 60, 0.5) 50%, transparent 100%),
      linear-gradient(165deg, var(--sun-glow) 0%, var(--front-mid) 40%, var(--front-deep) 75%, var(--front-shadow) 100%);
  }

  .spine-band { position: absolute; left: 573px; top: 0; width: 53px; height: 887px; background: var(--spine-tint); }

  /* Back cover */
  .back-heading {
    position: absolute; left: 47px; top: 50px; width: 497px;
    font-family: "Source Sans 3", sans-serif; font-weight: 700; font-size: 28px; line-height: 30px;
    letter-spacing: 0.36em; color: var(--ink); white-space: nowrap; text-align: center;
  }
  .back-blurb {
    position: absolute; left: 46px; top: 91px; width: 500px;
    font-size: 15.6px; line-height: 20.8px; color: var(--ink); text-align: center;
  }
  .back-blurb p + p { margin-top: 10px; }
  .author-photo {
    position: absolute; left: 48px; top: 396px; width: 181px; height: 238px;
    border: 3px solid var(--photo-frame);
    background: linear-gradient(160deg, #4e5a3a 0%, var(--photo-fill) 45%, #3a3026 100%);
  }
  .author-bio {
    position: absolute; left: 252px; top: 390px; width: 284px;
    font-size: 15.6px; line-height: 20.8px; color: var(--ink);
  }

  /* Spine */
  .spine-title, .spine-author {
    position: absolute; writing-mode: vertical-rl; white-space: nowrap;
    left: 573px; width: 53px; display: flex; align-items: center;
  }
  .spine-title {
    top: 52px; font-family: "Source Sans 3", sans-serif; font-weight: 700;
    font-size: 26px; letter-spacing: 0.38em; color: var(--ink);
  }
  .spine-author {
    top: 664px; font-family: "Fira Sans Extra Condensed", sans-serif; font-weight: 700;
    font-size: 38px; color: var(--paper);
  }

  /* Front cover */
  .front-author {
    position: absolute; left: 626px; width: 574px; top: 40px; text-align: center;
    font-family: "Fira Sans Extra Condensed", sans-serif; font-weight: 800;
    font-size: 70px; line-height: 1; color: var(--ink);
  }
  .front-subtitle {
    position: absolute; left: 626px; width: 574px; top: 497px; text-align: center;
    font-family: "Fira Sans Extra Condensed", sans-serif; font-weight: 700;
    font-size: 35px; line-height: 43px; color: var(--paper);
  }
  .front-title { position: absolute; left: 626px; width: 574px; top: 676px; text-align: center; color: var(--paper); }
  .front-title .title-article {
    display: block; font-family: "Fira Sans Extra Condensed", sans-serif; font-weight: 700;
    font-size: 44px; line-height: 44px;
  }
  .front-title .title-main {
    display: block; font-family: "Fira Sans Extra Condensed", sans-serif; font-weight: 700;
    font-size: 92px; line-height: 76px;
  }
  .front-title .title-tail {
    display: block; font-family: "Source Sans 3", sans-serif; font-weight: 300;
    font-size: 62px; line-height: 64px; letter-spacing: 0.5em; padding-left: 0.5em;
  }
</style>
</head>
<body>
<main class="cover-wrap">
  <div class="back-scene" role="img" aria-label="Sunrise over a misty forest, warm orange wash across the back cover"></div>
  <div class="front-scene" role="img" aria-label="Bright sun rising over silhouetted pine trees in orange and gold light"></div>
  <div class="spine-band"></div>

  <section class="back-cover">
    <h2 class="back-heading">THE BANKER'S RIDDLE</h2>
    <div class="back-blurb">
      <p>Here is an account of how new technology could reshape the way our economy works. Handled wisely, everyone comes out ahead. Paired with a fresh view of what money really is, innovation can remove the need for income taxes while balancing the budget and retiring the national debt. We could even fund a citizen income, tuition-free college, and universal healthcare, while sharply cutting poverty.</p>
      <p>The ideas presented here belong to no party and serve both wealthy and poor alike. They could lift our country to a level of prosperity it has never reached before. The key lies in rebuilding our financial system to fuel the productive power that technology unlocks, rather than taxing success as we do now.</p>
    </div>
    <div class="author-photo" role="img" aria-label="Portrait photo of the author outdoors"></div>
    <p class="author-bio">Hale helped shape structured finance on Wall Street, designed the funding plan for a major national rebuilding program, co-founded two award-winning charter schools, started several thriving technology firms and created a student magazine read by millions across many countries. A father of six, he splits his time with his wife between Oregon and Arizona, and likes nothing more than untangling big economic puzzles.</p>
  </section>

  <div class="spine-title">THE BANKER'S RIDDLE</div>
  <div class="spine-author">DEREK HALE</div>

  <section class="front-cover">
    <p class="front-author">DEREK HALE</p>
    <p class="front-subtitle">If Our Country Were Managed Wisely,<br>We Wouldn't Owe Taxes,<br>We'd Collect Returns</p>
    <h1 class="front-title">
      <span class="title-article">THE</span>
      <span class="title-main">BANKER'S</span>
      <span class="title-tail">RIDDLE</span>
    </h1>
  </section>
</main>
</body>
</html>
```